CedarBight.Lawyer, a new website for Morris.

Looking for a professional web site for my small country law firm.
I have a logo, chart, map, my photo, office photo, google analytics code, my drone video on YouTube, "Brantwell Beacon Skyrun, also on www.loftcove.guide", and text content. I am figuring out how to get those into digital forms.
First page needs a professional look. Here's where I am really hoping for your skill set.
Banner should be well designed so as to "ease" the viewer into confidence in my firm
Prefer the "white backround", less cluttered style of design.
My office has been in Key Center, main and only town of Key Peninsula, for 25 years, with emphasis on real property matters. Naturally land lasts longer than people, so estates, trusts and succession issues are relevant.
Local KP is the heart of southern Puget Sound, 75 miles of spectacular residential waterfront. We have the best land, waterfront, beaches and views in Puget Sound, however of course Seattle and the San Juan Islands could not be disregarded. It's that we have the most privacy, the best old growth Doug Firs, wildlife and low population density.
Puget Sound conditions are very specific for residential development.
One must consider:
Topography, hydro-geology, geomorphology, hill slope stability, soils must support septic systems, individual wells, prescriptive, express and implied easement issues, boundary lines don't always line up with surveys or expectations, or historic use, thus adverse possession abounds environmentally protected shorelines and wetlands, all challenges, but ohh.., the views and unique, world class waterfront.
Everyone who lives on Puget Sound is convinced they live in the most beautiful and spectacular place in the world, and we're all correct.

Target Market(s)

Members of the Halvern-Ostrow County Bar Association, and more distant counsel seeking consultation re: local conditions.
Also, I decided it was time to have a website, so a reference place to direct clients.
I like the professional sound of .lawyer vs. commercial sound of .com.

Industry/Entity Type

Law Firm

Coding

Coded - Design and coding required

Number of Pages Required

5+ page

Font styles to use
Other font styles liked:
• That newly created "web" font everyone seems to be usIng

Colors
32b8a4
3377b5

Requirements
Must have
• A strong first page with my photo and Puget Sound chart professionally created.
• A page I have ready with local links.
• A "How to find me page", which should have a map, and photo of my office, which I can make with the preloaded templates the host provides.
• A "This is what I do page", with some testimonials, which I can do via said templates or preferably by professionals.
Nice to have
• Clean look.
• Consistent looks to pages.
• First comment I got back talked about just designing one page, and if requires $340.00, so be it.
• Typical local sites have 4/5 pages, so perhaps a "fill-able" generic pages, I can build myself.
• Ideally, I would step into a working site I can edit myself.
• Not looking for e-commerce site, but the remainder of language the "Smart" professional used is unknown to me.
• Bit out of my element here, hoping for guidance.
Should not have
• Clutter

```html
<!DOCTYPE html>
<html lang="en">
<head>
<meta charset="utf-8">
<title>CedarBight.Lawyer</title>
<link href="https://fonts.googleapis.com/css2?family=Open+Sans:wght@400;600;700&display=swap" rel="stylesheet">
<style>
  :root {
    --navy: #1f2a7a;
    --ink: #222222;
    --title: #333333;
    --muted: #777777;
    --rule: #c9c9c9;
    --white: #ffffff;
    --footer: #0d0d0d;
    --hero-a: #3b5448;
    --hero-b: #1f3a5e;
    --hero-c: #142a48;
  }
  * { box-sizing: border-box; margin: 0; padding: 0; }
  html, body { width: 1200px; height: 2442px; overflow: hidden; }
  body {
    position: relative;
    background: var(--white);
    font-family: "Open Sans", Arial, sans-serif;
    color: var(--ink);
  }

  /* Hero */
  .hero {
    position: absolute; left: 0; top: 0; width: 1200px; height: 544px;
    background: linear-gradient(135deg, var(--hero-a) 0%, var(--hero-b) 45%, var(--hero-c) 100%);
  }
  .brand {
    position: absolute; left: 321px; top: 11px;
    display: flex; align-items: center; gap: 9px;
    color: var(--white); font-weight: 600; font-size: 16px; letter-spacing: 0.2px;
  }
  .brand-dot { width: 34px; height: 34px; border-radius: 50%; background: var(--white); }
  .main-nav, .footer-nav {
    position: absolute; width: 160px; height: 14px;
    font-size: 9.5px; font-weight: 600; color: var(--white); letter-spacing: 0.3px;
  }
  .main-nav { top: 23px; left: 772px; }
  .main-nav span, .footer-nav span { position: absolute; top: 0; white-space: nowrap; }
  .main-nav span:nth-child(1), .footer-nav span:nth-child(1) { left: 0; }
  .main-nav span:nth-child(2), .footer-nav span:nth-child(2) { left: 53px; }
  .main-nav span:nth-child(3), .footer-nav span:nth-child(3) { left: 103px; }
  .hero-caption { position: absolute; left: 308px; top: 193px; width: 296px; color: var(--white); }
  .hero-title { font-size: 21px; font-weight: 600; letter-spacing: 0.6px; }
  .hero-rule { width: 49px; height: 2px; background: var(--white); margin: 8px 0 12px; }
  .hero-text { font-size: 9.8px; line-height: 13.2px; letter-spacing: 0.3px; }
  .slider-arrow {
    position: absolute; top: 271px; width: 32px; height: 32px; border-radius: 50%;
    background: rgba(20,20,20,0.75);
  }
  .slider-arrow svg { display: block; }
  .slider-arrow.prev { left: 86px; }
  .slider-arrow.next { left: 1045px; }

  /* Section headings */
  .section-title {
    position: absolute; left: 0; width: 1200px; text-align: center;
    color: var(--navy); font-size: 21px; font-weight: 700; letter-spacing: 0.8px;
  }
  .section-rule { position: absolute; left: 571px; width: 58px; height: 5px; background: var(--rule); }

  /* News */
  .news-list { position: absolute; left: 241px; top: 668px; width: 720px; }
  .article { display: flex; height: 268px; }
  .article.flip { flex-direction: row-reverse; }
  .article-photo { width: 360px; height: 268px; flex: none; }
  .article-body { position: relative; width: 360px; height: 268px; background: var(--white); z-index: 1; }
  .article-body::before {
    content: ""; position: absolute; top: 114px; left: -20px;
    border-top: 20px solid transparent; border-bottom: 20px solid transparent;
    border-right: 20px solid var(--white);
  }
  .article.flip .article-body::before {
    left: auto; right: -20px; border-right: 0; border-left: 20px solid var(--white);
  }
  .article-title, .article-date, .article-rule, .article-text, .btn-read { position: absolute; left: 33px; }
  .article.flip .article-title, .article.flip .article-date, .article.flip .article-rule,
  .article.flip .article-text, .article.flip .btn-read { left: 36px; }
  .article-title { top: 16px; font-size: 17.5px; font-weight: 600; color: var(--title); letter-spacing: 0.4px; }
  .article-date { top: 62px; font-size: 7.5px; color: var(--muted); }
  .article-rule { top: 76px; width: 58px; height: 1px; background: #999; }
  .article-text { top: 88px; width: 282px; font-size: 9.2px; line-height: 12.7px; color: var(--ink); }
  .btn-read {
    top: 214px; width: 98px; height: 25px;
    display: flex; align-items: center; justify-content: center;
    border: 1.5px solid var(--navy); border-radius: 4px;
    font-size: 7.5px; font-weight: 700; letter-spacing: 0.4px; color: var(--ink);
  }
  .photo-sunset { background: linear-gradient(160deg, #8a7f9c 0%, #c98f7a 55%, #4a4656 100%); }
  .photo-sunset-two { background: linear-gradient(200deg, #9a8aa6 0%, #d09a88 55%, #4e4650 100%); }
  .photo-gavel { background: linear-gradient(160deg, #a4875f 0%, #cdb489 60%, #8a6a48 100%); }
  .photo-books { background: linear-gradient(160deg, #cbb89a 0%, #9a5a48 60%, #5a3a30 100%); }
  .photo-court { background: linear-gradient(160deg, #c07a3e 0%, #a86232 60%, #6a3c20 100%); }

  .btn-more {
    position: absolute; left: 518px; top: 2072px; width: 160px; height: 41px;
    border: 2px solid var(--navy); border-radius: 5px;
    display: flex; align-items: center; justify-content: center;
    font-size: 13px; font-weight: 600; letter-spacing: 0.5px; color: var(--ink);
  }

  /* About */
  .about-col { position: absolute; top: 2259px; font-size: 7.2px; line-height: 11.4px; color: #444; }
  .about-col.left { left: 260px; width: 312px; }
  .about-col.right { left: 622px; width: 316px; }
  .about-divider { position: absolute; left: 955px; top: 2259px; width: 1px; height: 102px; background: #bbb; }

  /* Footer */
  .site-footer { position: absolute; left: 0; top: 2400px; width: 1200px; height: 42px; background: var(--footer); }
  .copyright { position: absolute; left: 249px; top: 16px; font-size: 7px; color: #888; }
  .footer-nav { top: 15px; left: 772px; font-size: 8.5px; }
</style>
</head>
<body>

<header class="hero" role="img" aria-label="Aerial view of a harbor inlet with waterfront homes, marina and kayakers">
  <div class="brand"><span class="brand-dot"></span>CedarBight.Lawyer</div>
  <nav class="main-nav"><span>HOME</span><span>NEWS</span><span>ABOUT US</span></nav>
  <div class="hero-caption">
    <h1 class="hero-title">BRANTWELL BAY</h1>
    <div class="hero-rule"></div>
    <p class="hero-text">It is a long established fact that a reader will be distracted by the readable content of a page when looking at its layout. The point of using Lorem Ipsum is that it has a more-or-less normal distribution of letters opposed to using 'Content here, content here', making it look like readable English. Many desktop publishing packages and web page editors now use Lorem Ipsum as their default model text.</p>
  </div>
  <span class="slider-arrow prev"><svg width="32" height="32" viewBox="0 0 32 32"><path d="M18 10 L12 16 L18 22" fill="none" stroke="#fff" stroke-width="2"/></svg></span>
  <span class="slider-arrow next"><svg width="32" height="32" viewBox="0 0 32 32"><path d="M14 10 L20 16 L14 22" fill="none" stroke="#fff" stroke-width="2"/></svg></span>
</header>

<h2 class="section-title" style="top:584px">NEWS</h2>
<div class="section-rule" style="top:623px"></div>

<section class="news-list">
  <article class="article">
    <div class="article-photo photo-sunset" role="img" aria-label="Sunset over calm sound waters with distant mountains"></div>
    <div class="article-body">
      <h3 class="article-title">ARTICLE TITILE</h3>
      <p class="article-date">01/01/2016</p><div class="article-rule"></div>
      <p class="article-text">Lorem Ipsum is simply dummy text of the printing and typesetting industry. Lorem Ipsum has been the industry's standard dummy text ever since the 1500s, when an unknown printer took a galley of type and scrambled it to make a type specimen book. It has survived not only five centuries, but also the leap into electronic typesetting, remaining essentially unchanged. It was popularised in the 1960s with the release of Letraset sheets containing Lorem Ipsum passages, and more</p>
      <span class="btn-read">READ MORE</span>
    </div>
  </article>
  <article class="article flip">
    <div class="article-photo photo-sunset-two" role="img" aria-label="Pink sunset over the water framed by evergreen branches"></div>
    <div class="article-body">
      <h3 class="article-title">ARTICLE TITILE</h3>
      <p class="article-date">01/01/2016</p><div class="article-rule"></div>
      <p class="article-text">Lorem Ipsum is simply dummy text of the printing and typesetting industry. Lorem Ipsum has been the industry's standard dummy text ever since the 1500s, when an unknown printer took a galley of type and scrambled it to make a type specimen book. It has survived not only five centuries, but also the leap into electronic typesetting, remaining essentially unchanged. It was popularised in the 1960s with the release of Letraset sheets containing Lorem Ipsum passages, and more</p>
      <span class="btn-read">READ MORE</span>
    </div>
  </article>
  <article class="article">
    <div class="article-photo photo-gavel" role="img" aria-label="Wooden gavel resting on an open law book"></div>
    <div class="article-body">
      <h3 class="article-title">ARTICLE TITILE</h3>
      <p class="article-date">01/01/2016</p><div class="article-rule"></div>
      <p class="article-text">Lorem Ipsum is simply dummy text of the printing and typesetting industry. Lorem Ipsum has been the industry's standard dummy text ever since the 1500s, when an unknown printer took a galley of type and scrambled it to make a type specimen book. It has survived not only five centuries, but also the leap into electronic typesetting, remaining essentially unchanged. It was popularised in the 1960s with the release of Letraset sheets containing Lorem Ipsum passages, and more</p>
      <span class="btn-read">READ MORE</span>
    </div>
  </article>
  <article class="article flip">
    <div class="article-photo photo-books" role="img" aria-label="Row of leather-bound law books on a shelf"></div>
    <div class="article-body">
      <h3 class="article-title">ARTICLE TITILE</h3>
      <p class="article-date">01/01/2016</p><div class="article-rule"></div>
      <p class="article-text">Lorem Ipsum is simply dummy text of the printing and typesetting industry. Lorem Ipsum has been the industry's standard dummy text ever since the 1500s, when an unknown printer took a galley of type and scrambled it to make a type specimen book. It has survived not only five centuries, but also the leap into electronic typesetting, remaining essentially unchanged. It was popularised in the 1960s with the release of Letraset sheets containing Lorem Ipsum passages, and more</p>
      <span class="btn-read">READ MORE</span>
    </div>
  </article>
  <article class="article">
    <div class="article-photo photo-court" role="img" aria-label="Brass scales of justice in front of a warm-lit courtroom"></div>
    <div class="article-body">
      <h3 class="article-title">ARTICLE TITILE</h3>
      <p class="article-date">01/01/2016</p><div class="article-rule"></div>
      <p class="article-text">Lorem Ipsum is simply dummy text of the printing and typesetting industry. Lorem Ipsum has been the industry's standard dummy text ever since the 1500s, when an unknown printer took a galley of type and scrambled it to make a type specimen book. It has survived not only five centuries, but also the leap into electronic typesetting, remaining essentially unchanged. It was popularised in the 1960s with the release of Letraset sheets containing Lorem Ipsum passages, and more</p>
      <span class="btn-read">READ MORE</span>
    </div>
  </article>
</section>

<span class="btn-more">MORE NEWS</span>

<h2 class="section-title" style="top:2179px">ABOUT US</h2>
<div class="section-rule" style="top:2217px"></div>

<p class="about-col left">Lorem Ipsum is simply dummy text of the printing and typesetting industry. Lorem Ipsum has been the industry's standard dummy text ever since the 1500s, when an unknown printer took a galley of type and scrambled it to make a type specimen book. It has survived not only five centuries, but also the leap into electronic typesetting, remaining essentially unchanged. It was popularised in the 1960s with the release of Letraset sheets containing Lorem Ipsum passages, and more recently with desktop publishing software like Aldus PageMaker including versions of Lorem Ipsum. Lorem Ipsum is simply dummy text of the printing and typesetting industry. Lorem Ipsum has been the industry's</p>
<p class="about-col right">Lorem Ipsum is simply dummy text of the printing and typesetting industry. Lorem Ipsum has been the industry's standard dummy text ever since the 1500s, when an unknown printer took a galley of type and scrambled it to make a type specimen book. It has survived not only five centuries, but also the leap into electronic typesetting, remaining essentially unchanged. It was popularised in the 1960s with the release of Letraset sheets containing Lorem Ipsum passages, and more recently with desktop publishing software like Aldus PageMaker including versions of Lorem Ipsum. Lorem Ipsum is simply dummy text of the printing and typesetting industry. Lorem Ipsum has been the industry's</p>
<div class="about-divider"></div>

<footer class="site-footer">
  <p class="copyright">© 2015 - Copyright</p>
  <nav class="footer-nav"><span>HOME</span><span>NEWS</span><span>ABOUT US</span></nav>
</footer>

</body>
</html>
```